Carpet and Flooring business needs a leaflet/flyer design

Brackenridge Floors is a small carpet and flooring business looking for a flyer to be printed on double sided A6 postcard. As a home based business the flyer is to inform local people of our existence, our services and our ability to genuinely save them money. (We dont do gimmicks and fake sales!). As this flyer will be delivered to mainly households it should be more carpet than flooring.

How we operate as a home based business is that once we receive a call from a potential customer we try and discover a bit more about their requirements and budget, we then arrange to visit them to measure up and to show them a selection of samples based on the initial call. Normally we get this right first time, if not we will return at a later date with more samples. We then give the quote and hopefully get the order.

We sell all the makes and ranges you will find in the shops but for a lot less. We do all qualities from entry level (7.99M2) to top end. We do not however get involved with 'cheap carpets'.... these so called carpets offer a false economy and don't do our reputation any good.

Target Market(s)

home owners, landlords, estate agents, people that need carpet

Industry/Entity Type

Flooring

Requirements
Must have
• Phone Number - 01432 517804
Nice to have
• more emphasise on carpets

local
honest
reliable
experienced
professional
friendly
value for money

Should not have
• No mention of 'cheap carpets'
No cartoon characters carrying a roll of carpet.
No flying or magic carpets.

```html
<!DOCTYPE html>
<html lang="en">
<head>
<meta charset="utf-8">
<title>Brackenridge Floors – A6 Flyer</title>
<link rel="stylesheet" href="https://fonts.googleapis.com/css2?family=Marcellus+SC&family=Crimson+Text:wght@400;700&display=swap">
<style>
  :root {
    --orange: #e8794b;
    --orange-deep: #d9653a;
    --green: #a9c37d;
    --peach: #fde7d4;
    --peach-soft: #fff4ea;
    --ink: #2a2622;
    --paper: #ffffff;
    --backdrop: #e6e6e4;
    --head-font: "Marcellus SC", serif;
    --body-font: "Crimson Text", serif;
  }
  * { box-sizing: border-box; margin: 0; padding: 0; }
  html, body { width: 1200px; height: 900px; overflow: hidden; }
  body { background: var(--backdrop); position: relative; font-family: var(--body-font); color: var(--ink); }

  .flyer {
    position: absolute; top: 90px; width: 500px; height: 720px;
    background: var(--paper); overflow: hidden;
    box-shadow: 0 2px 10px rgba(0,0,0,0.18);
  }
  .flyer--back { left: 80px; }
  .flyer--front { left: 620px; }

  /* Back side */
  .swatch-strip {
    height: 95px;
    background: linear-gradient(90deg, #b3541f 0%, #d9722b 18%, #c98f4c 34%, #e9a25f 50%, #eeb46f 66%, #f3c98a 82%, #f6dca6 100%);
  }
  .headline-band {
    background: linear-gradient(180deg, var(--peach) 0%, var(--peach-soft) 100%);
    border-top: 6px solid var(--orange);
    padding: 12px 22px 14px;
    text-align: center;
  }
  .headline-band h1 {
    font-family: var(--head-font); font-weight: 400;
    color: var(--orange); font-size: 24px; line-height: 1.15; letter-spacing: 0.5px;
  }
  .brand {
    display: flex; align-items: center; justify-content: center; gap: 10px;
    margin: 18px 0 14px;
  }
  .brand__mark { width: 26px; height: 26px; background: var(--green); }
  .brand__name {
    font-family: var(--head-font); font-weight: 400; color: var(--orange);
    font-size: 30px; letter-spacing: 0.5px;
  }
  .service-list { list-style: none; padding: 0 28px 0 34px; }
  .service-list li {
    position: relative; font-size: 13.6px; line-height: 1.22; margin-bottom: 11px; padding-left: 4px;
  }
  .service-list li::before {
    content: ""; position: absolute; left: -18px; top: 4px;
    width: 9px; height: 9px; transform: rotate(45deg); background: var(--orange);
  }
  .service-list li:nth-child(even)::before { background: var(--green); }

  .call-band {
    position: absolute; left: 0; right: 0; bottom: 0; height: 56px;
    background: var(--green); display: flex; align-items: center; justify-content: center;
  }
  .call-band p { color: #fff; font-family: var(--body-font); font-weight: 700; font-size: 25px; letter-spacing: 0.5px; }

  /* Front side */
  .hero-photo {
    position: absolute; left: 0; top: 0; width: 500px; height: 450px;
    background: linear-gradient(160deg, #c9c1b8 0%, #b7aea4 40%, #8d8078 70%, #c3b7a9 100%);
  }
  .hero-curve { position: absolute; left: 0; top: 360px; width: 500px; height: 110px; }
  .brand-plate {
    position: absolute; left: 12px; top: 120px; width: 220px; height: 95px;
    background: rgba(255,255,255,0.72);
    display: flex; align-items: center; justify-content: center; gap: 8px;
  }
  .brand-plate .brand__name { font-size: 21px; }
  .brand-plate .brand__mark { width: 20px; height: 20px; }
  .front-message {
    position: absolute; left: 0; right: 0; top: 485px; text-align: center;
    font-family: var(--head-font); color: var(--orange);
  }
  .front-message .question { font-size: 28px; line-height: 1.22; }
  .front-message .answer { font-size: 31px; margin-top: 4px; color: var(--orange-deep); text-shadow: 0.5px 0 0 var(--orange-deep); }
</style>
</head>
<body>

<section class="flyer flyer--back" aria-label="Flyer reverse side">
  <div class="swatch-strip" role="img" aria-label="Row of carpet samples in warm orange and cream tones"></div>
  <header class="headline-band">
    <h1>Looking for a local carpet and flooring company that will give you great products and save you money?</h1>
  </header>
  <div class="brand">
    <span class="brand__mark"></span>
    <span class="brand__name">Brackenridge Floors</span>
  </div>
  <ul class="service-list">
    <li>Upon visiting you at your home or office (which comes at no cost to you), we allow you to select your preferred carpet or flooring, while we measure up the area that you would like for this to cover and give you a free quote. This is of great importance as it helps you in saving on your budget by buying only what is required.</li>
    <li>We have a huge array of flooring and carpet products that you can opt to choose from that are guaranteed to improve the aesthetics of your home or even business premises. The designs of our products range from traditional to modern, ensuring that all your needs are covered.</li>
    <li>With our personnel boasting of experience in excess of 27 years, you are assured of us performing a great job for you in the laying of the floor or carpeting. Further, we give a guarantee on any workmanship that we undertake.</li>
    <li>All our products come from renowned manufacturers to enable us to supply the best value for money carpets and flooring to suit your budget.</li>
    <li>We supply and install all the latest products including carpet, laminate flooring, vinyl, carpet tiles and also luxury vinyl tiles. Brackenridge Floors offer you the peace of mind of working with experienced professionals when working on your next flooring project.</li>
  </ul>
  <footer class="call-band"><p>Call us: 01432 517804</p></footer>
</section>

<section class="flyer flyer--front" aria-label="Flyer front side">
  <div class="hero-photo" role="img" aria-label="Photo of a woman browsing a fan of carpet sample swatches"></div>
  <svg class="hero-curve" viewBox="0 0 500 110" preserveAspectRatio="none" aria-hidden="true">
    <path d="M0 110 L0 95 Q250 -10 500 20 L500 110 Z" fill="#fde7d4"/>
    <path d="M0 110 L0 105 Q250 10 500 40 L500 110 Z" fill="#ffffff"/>
  </svg>
  <div class="brand-plate">
    <span class="brand__mark"></span>
    <span class="brand__name">Brackenridge Floors</span>
  </div>
  <div class="front-message">
    <p class="question">Where is the best place to<br>buy carpets and flooring?</p>
    <p class="answer">That's easy... it's your place!</p>
  </div>
  <footer class="call-band"><p>Call us: 01432 517804</p></footer>
</section>

</body>
</html>
```